Presentation brochure Le Bourdon

We need a brochure presenting our training and our school. We are a building training center and have deployed our first training course on plumbing.
We already have a website as well as original illustrations which are the essence of our graphic charter.
The idea would be to take the assets made available and create a 6-page brochure, with 3 pages on the School and 3 pages on the training and its program. Attached are screenshots of the website with the information to highlight.
The creation would ideally be in shades of purple and yellow.
The design must inspire the excellence of our training and the innovation of our concept.
Design size is A4 sheet folded in 3 (i.e. 9.9 x 21 per page)
Target Market(s)
Individuals and Professional Craftsmen
Industry/Entity Type
Bâtiment
Font styles to use
Other font styles liked:
- Pour les titres, Aller Display
Look and feel

```html
<!DOCTYPE html>
<html lang="fr">
<head>
<meta charset="utf-8">
<title>Le Bourdon – Brochure Formation Plomberie</title>
<link rel="stylesheet" href="https://fonts.googleapis.com/css2?family=Poppins:wght@400;500;600;700&family=Montserrat:wght@400;500&display=swap">
<style>
:root{
  --purple:#5a52a8;
  --purple-deep:#4b4497;
  --purple-soft:#7b74c2;
  --yellow:#f2b03c;
  --peach:#f8e2d3;
  --paper:#ffffff;
  --grey:#f1f1f4;
  --stage:#dcdcde;
  --ink-soft:#6d68a8;
}
*{margin:0;padding:0;box-sizing:border-box}
html,body{width:864px;height:1200px;overflow:hidden;background:var(--stage)}
body{position:relative;font-family:"Montserrat",sans-serif;color:var(--purple)}
.spread{position:absolute;left:32px;width:800px;height:566px;background:var(--paper);overflow:hidden;box-shadow:0 6px 18px rgba(0,0,0,.15)}
.spread--outside{top:24px}
.spread--inside{top:610px}
.shapes{position:absolute;inset:0;width:800px;height:566px}
.fold{position:absolute;top:0;bottom:0;width:1px;background:rgba(0,0,0,.06)}
.panel{position:absolute;top:0;height:566px;width:266.67px}
.panel--1{left:0}.panel--2{left:266.67px}.panel--3{left:533.33px}
.abs{position:absolute}
.photo,.art{position:absolute}
h1,h2,h3,.title{font-family:"Poppins",sans-serif}
.brand{font-family:"Poppins",sans-serif;font-weight:700;color:var(--purple);display:flex;align-items:center;gap:6px;white-space:nowrap}
.brand-dot{width:10px;height:10px;border-radius:50%;background:var(--purple)}
.tagline{font-family:"Montserrat",sans-serif;font-size:7px;color:var(--purple);text-align:center}
.checklist{list-style:none}
.checklist li{position:relative;padding-left:16px;font-size:6.4px;line-height:1.35;margin-bottom:5px;color:#fff}
.checklist li::before{content:"";position:absolute;left:0;top:1px;width:7px;height:7px;border:1px solid rgba(255,255,255,.8);border-radius:50%}
.checklist li::after{content:"";position:absolute;left:2px;top:3px;width:3px;height:1.5px;border-left:1px solid #fff;border-bottom:1px solid #fff;transform:rotate(-45deg)}
.list-head{font-family:"Poppins",sans-serif;font-weight:600;font-size:7.4px;color:#fff;margin:7px 0 6px}
.feature{position:absolute;width:110px}
.feature-icon{width:14px;height:14px;border-radius:3px;background:var(--purple);display:flex;align-items:center;justify-content:center;margin-bottom:4px}
.feature h3{font-size:8px;font-weight:700;line-height:1.1;margin-bottom:4px;color:var(--purple)}
.feature p{font-size:6px;line-height:1.35;color:var(--ink-soft)}
.contact{font-size:7px;line-height:1.5;text-align:center;color:#333}
.hero-box{position:absolute;left:40px;top:272px;width:227px;height:250px;background:linear-gradient(160deg,var(--purple-soft),var(--purple-deep));border-radius:30px 0 0 30px;padding:26px 18px 0 22px;color:#fff}
.hero-box h1{font-size:28px;font-weight:700;line-height:1.05;margin-bottom:22px}
.hero-box p{font-family:"Poppins",sans-serif;font-weight:600;font-size:12px;line-height:1.25}
.header-title{font-size:9px;font-weight:600;color:#fff;line-height:1}
.caps{font-size:7.6px;line-height:1.3;text-transform:uppercase;color:var(--purple);letter-spacing:.2px}
.section-title{font-size:11px;font-weight:700;line-height:1.2;color:var(--purple)}
.body-text p{font-size:6.6px;line-height:1.4;color:#444;margin-bottom:8px}
.info{position:absolute;display:flex;gap:6px}
.info svg{flex:none;margin-top:1px}
.info b{display:block;font-family:"Poppins",sans-serif;font-size:6.6px;font-weight:600;color:#333}
.info span{display:block;font-size:5.6px;line-height:1.35;color:#8a8a96}
.info a{font-size:5.6px;color:var(--purple);text-decoration:none}
</style>
</head>
<body>

<section class="spread spread--outside" aria-label="Extérieur de la brochure">
  <div class="photo" role="img" aria-label="Photo de l'atelier de formation : box cloisonnés, établis et sol en OSB" style="left:0;top:300px;width:533px;height:266px;background:linear-gradient(180deg,#d6d4cf 0%,#c9c2b2 55%,#b8ad92 78%,#c3c6c9 100%)"></div>
  <div class="photo" role="img" aria-label="Photo d'une installation sanitaire : WC raccordé aux tuyaux cuivre et multicouche" style="left:533px;top:0;width:267px;height:160px;background:linear-gradient(160deg,#d8d9da,#a7a6a3 55%,#c2ae8c)"></div>

  <svg class="shapes" viewBox="0 0 800 566" aria-hidden="true">
    <defs>
      <linearGradient id="g-purple" x1="0" y1="0" x2="1" y2="1">
        <stop offset="0" stop-color="#6a63b6"/><stop offset="1" stop-color="#4b4497"/>
      </linearGradient>
    </defs>
    <path d="M0 0 H267 V205 C230 250 150 290 70 296 L0 300 Z" fill="url(#g-purple)"/>
    <path d="M267 0 H533 V300 L533 322 C470 310 380 312 267 330 Z" fill="#fff"/>
    <path d="M267 0 C320 14 380 18 430 0 Z" fill="#ececf2"/>
    <path d="M533 120 C600 150 700 170 800 140 V566 H533 Z" fill="#fff"/>
  </svg>

  <div class="fold" style="left:266px"></div>
  <div class="fold" style="left:533px"></div>

  <div class="panel panel--1">
    <div class="abs" style="left:18px;top:26px;width:236px">
      <p class="list-head" style="margin-top:0">Téléchargez le programme</p>
      <ul class="checklist">
        <li>Intégrer les principes de développement durable</li>
        <li>Réaliser l'installation complète d'une salle de bain : montage d'un lavabo, d'une douche, d'un WC, raccordement via multicouche, cuivre, PER et évacuation en PVC</li>
      </ul>
      <p class="list-head">Vous aurez également acquis un savoir considérable et connaîtrez :</p>
      <ul class="checklist">
        <li>Les principales normes en vigueur du DTU 60</li>
        <li>Les notions essentielles sur l'eau</li>
        <li>Les notions d'étanchéité, d'évacuation et les bases pour l'installation d'un appareil sanitaire</li>
        <li>Les propriétés et règles d'installation du cuivre, du PER, du multicouche et du PVC</li>
        <li>Les moyens de production d'eau chaude sanitaire</li>
        <li>Et bien plus encore</li>
      </ul>
      <p class="list-head">Vous obtiendrez à l'issue de votre formation :</p>
      <p style="font-size:6.4px;color:#fff;padding-left:16px">Attestation de fin de formation</p>
    </div>
  </div>

  <div class="panel panel--2">
    <div class="abs" style="left:0;width:267px;top:40px;display:flex;flex-direction:column;align-items:center">
      <div class="brand" style="font-size:15px"><span class="brand-dot"></span>Le Bourdon</div>
      <p class="tagline">Apprendre vite et bien</p>
      <svg width="12" height="12" viewBox="0 0 12 12" style="margin:8px 0 4px" aria-hidden="true"><path d="M3 1.5h2l1 2.5-1.3 1a6 6 0 0 0 2.3 2.3l1-1.3 2.5 1v2a1 1 0 0 1-1 1A8.5 8.5 0 0 1 2 2.5a1 1 0 0 1 1-1Z" fill="none" stroke="#5a52a8" stroke-width="1"/></svg>
      <p class="contact">WWW.LEBOURDON-FORMATION.FR<br>+33 1 00 00 00 00<br>CONTACT@LEBOURDON-FORMATION.FR</p>
    </div>
    <div class="feature" style="left:18px;top:150px">
      <div class="feature-icon"><svg width="9" height="9" viewBox="0 0 9 9"><circle cx="4.5" cy="3.5" r="2.5" fill="none" stroke="#fff"/><path d="M3 6l-1 3 2.5-1.2L7 9 6 6" fill="none" stroke="#fff" stroke-width=".8"/></svg></div>
      <h3>Excellence<br>académique</h3>
      <p>Apprenez avec des artisans professionnels en activité et obtenez un diplôme reconnu par les entreprises</p>
    </div>
    <div class="feature" style="left:142px;top:150px">
      <div class="feature-icon"><svg width="9" height="9" viewBox="0 0 9 9"><circle cx="4.5" cy="2.5" r="1.6" fill="#fff"/><path d="M1.5 8.5a3 3 0 0 1 6 0Z" fill="#fff"/></svg></div>
      <h3>Encadrement<br>efficace</h3>
      <p>Nos promotions sont limitées à 20 élèves maximum favorisant un encadrement efficace par le professeur</p>
    </div>
    <div class="feature" style="left:18px;top:232px">
      <div class="feature-icon"><svg width="9" height="9" viewBox="0 0 9 9"><circle cx="3" cy="3" r="1.4" fill="#fff"/><circle cx="6.5" cy="3" r="1.4" fill="#fff"/><path d="M.5 8a2.5 2.5 0 0 1 5 0ZM4 8a2.5 2.5 0 0 1 5 0Z" fill="#fff"/></svg></div>
      <h3>Expérience<br>humaine</h3>
      <p>Particuliers et professionnels constituent nos promotions favorisant l'échange et l'entraide pour une expérience humaine inoubliable</p>
    </div>
    <div class="feature" style="left:142px;top:232px">
      <div class="feature-icon"><svg width="9" height="9" viewBox="0 0 9 9"><path d="M1.5 7.5l4-4M5 1.5l2.5 2.5M7.5 7.5l-4-4M1.5 1.5 4 4" stroke="#fff" stroke-width="1.1" stroke-linecap="round"/></svg></div>
      <h3>Mises en situation</h3>
      <p>Nos exercices pratiques en box individuel reproduisent des travaux en situation réelle pour que nos élèves soient le plus rapidement opérationnel</p>
    </div>
  </div>

  <div class="panel panel--3">
    <div class="abs" style="left:0;width:267px;top:180px;display:flex;flex-direction:column;align-items:center">
      <div class="brand" style="font-size:20px"><span class="brand-dot" style="width:13px;height:13px"></span>Le Bourdon</div>
      <p class="tagline" style="font-size:8px">Apprendre vite et bien</p>
    </div>
    <div class="hero-box">
      <h1>Formation<br>Plomberie</h1>
      <p>Maitrisez les fondamentaux de Plomberie en seulement 1 semaine !</p>
    </div>
  </div>
</section>

<section class="spread spread--inside" aria-label="Intérieur de la brochure">
  <div class="art" role="img" aria-label="Illustration : deux artisans travaillant dans un box d'atelier avec échelle, horloge et meuble à tiroirs" style="left:0;top:30px;width:533px;height:250px;background:linear-gradient(180deg,#fbeadf 0%,#f6d9c6 70%,#f1cdb6 100%)"></div>

  <svg class="shapes" viewBox="0 0 800 566" aria-hidden="true">
    <defs>
      <linearGradient id="g-purple2" x1="0" y1="0" x2="1" y2="1">
        <stop offset="0" stop-color="#6a63b6"/><stop offset="1" stop-color="#4b4497"/>
      </linearGradient>
    </defs>
    <path d="M0 28 H200 C230 28 248 40 267 52 V80 C230 90 210 120 170 122 L0 122 Z" fill="url(#g-purple2)"/>
    <path d="M0 280 C150 288 350 270 533 260 V566 H0 Z" fill="#fff"/>
    <path d="M267 280 H533 V566 H267 Z" fill="#fff"/>
    <path d="M533 0 H800 V250 C720 300 620 320 533 330 Z" fill="url(#g-purple2)"/>
    <path d="M533 330 C620 320 720 300 800 250 V566 H533 Z" fill="#f4f4f7"/>
  </svg>

  <div class="art" role="img" aria-label="Illustration : outils et objets de l'apprentissage mobile, équerre, clé, smartphone, livre, multimètre" style="left:30px;top:412px;width:206px;height:140px;border-radius:10px;background:linear-gradient(135deg,#e4e0f4 0%,#f5e6d6 55%,#f7d9a8 100%)"></div>

  <div class="fold" style="left:266px"></div>
  <div class="fold" style="left:533px"></div>

  <div class="panel panel--1">
    <div class="abs" style="left:18px;top:50px">
      <h2 class="header-title">Formation Plomberie</h2>
      <p class="header-title" style="margin-top:12px">Temps plein (1 semaine)</p>
    </div>
    <p class="caps abs" style="left:34px;top:306px;width:200px">En une semaine de formation intensive mélangeant théorie en digital et pratique sur notre campus encadré par un artisan professionnel, apprenez toutes les compétences d'un plombier pour vous lancer dans vos travaux ou changer de carrière.</p>
  </div>

  <div class="panel panel--2">
    <h2 class="section-title abs" style="left:22px;top:298px;width:230px">Maitrisez les fondamentaux de Plomberie en seulement 1 semaine !</h2>
    <div class="body-text abs" style="left:22px;top:340px;width:225px">
      <p>Les formations de plomberie sont longues et coûteuses. Le Bourdon a construit un programme intense qui va à l'essentiel pour les débutants comme pour les artisans confirmés. Notre secret ? Nous avons déporté toute la partie théorique via un apprentissage ludique en mobile learning :</p>
      <p>de courtes vidéos accessibles partout, de la gamification pour se tester et des fiches essentielles pour mémoriser les notions fondamentales.</p>
      <p>La semaine que vous passerez sur notre campus sera donc consacrée quasi exclusivement à la pratique où vous serez encadré par un artisan professionnel. Notre communauté de Bourdonneurs grandit vite. Venez vivre une expérience unique !</p>
    </div>
    <div class="abs" style="left:22px;top:512px">
      <div class="brand" style="font-size:14px"><span class="brand-dot"></span>Le Bourdon</div>
      <p class="tagline" style="text-align:left;padding-left:16px">Apprendre vite et bien</p>
    </div>
  </div>

  <div class="panel panel--3">
    <div class="abs" style="left:20px;top:26px;width:232px">
      <h2 class="title" style="font-size:9.5px;font-weight:600;color:#fff;line-height:1.25;margin-bottom:10px">A l'issue de cette formation, vous serez capable de</h2>
      <ul class="checklist">
        <li>Identifier les éléments d'une installation de plomberie</li>
        <li>Travailler le cuivre : brasure, cintrage, réalisation de collets battus, baïonnettes</li>
        <li>Monter un appareil sanitaire raccordé à l'alimentation et à l'évacuation</li>
        <li>Modifier une installation sanitaire existante (arrivée d'eau, lavabo, machine à laver)</li>
        <li>Réaliser l'installation d'un réseau d'eau chaude sanitaire via le montage d'un ballon d'eau chaude sanitaire et de ses accessoires</li>
        <li>Diagnostiquer un dysfonctionnement sur un réseau sanitaire et y remédier</li>
        <li>Réaliser la maintenance courante, préventive et améliorative des équipements</li>
        <li>Intégrer les principes de développement durable</li>
      </ul>
    </div>

    <div class="info" style="left:20px;top:352px;width:110px">
      <svg width="10" height="10" viewBox="0 0 10 10"><circle cx="3.5" cy="3" r="1.6" fill="#5a52a8"/><circle cx="7" cy="3.3" r="1.3" fill="#5a52a8"/><path d="M.5 9a3 3 0 0 1 6 0ZM5.5 9a2.5 2.5 0 0 1 4 0Z" fill="#5a52a8"/></svg>
      <div><b>Public :</b><span>Particulier et professionnel</span></div>
    </div>
    <div class="info" style="left:20px;top:382px;width:110px">
      <svg width="10" height="10" viewBox="0 0 10 10"><circle cx="5" cy="5" r="4" fill="none" stroke="#5a52a8" stroke-width="1.2"/><path d="M5 1v4h4a4 4 0 0 0-4-4Z" fill="#5a52a8"/></svg>
      <div><b>Durée formation :</b><span>1 semaine(s)</span></div>
    </div>
    <div class="info" style="left:20px;top:412px;width:110px">
      <svg width="10" height="10" viewBox="0 0 10 10"><path d="M5 9.5S1.8 6 1.8 4a3.2 3.2 0 0 1 6.4 0C8.2 6 5 9.5 5 9.5Z" fill="#5a52a8"/><circle cx="5" cy="4" r="1.2" fill="#fff"/></svg>
      <div><b>Lieu :</b><span>Campus Paris (Marne la Vallée)</span></div>
    </div>
    <div class="info" style="left:20px;top:442px;width:110px">
      <svg width="10" height="10" viewBox="0 0 10 10"><rect x="1" y="2" width="8" height="7" rx="1" fill="none" stroke="#5a52a8" stroke-width="1.1"/><path d="M1 4h8M3 1v2M7 1v2" stroke="#5a52a8" stroke-width="1.1"/></svg>
      <div><b>Sessions :</b><span>26 Octobre 2022</span></div>
    </div>
    <p class="title abs" style="left:22px;top:486px;font-size:8px;font-weight:700;line-height:1.15;color:var(--purple)">Formation<br>Plomberie</p>

    <div class="info" style="left:140px;top:352px;width:115px">
      <svg width="10" height="10" viewBox="0 0 10 10"><path d="M1 5V1h4l4.5 4.5-4 4Z" fill="#5a52a8"/><circle cx="3" cy="3" r=".9" fill="#fff"/></svg>
      <div><b>Tarif :</b><span>1890 €</span></div>
    </div>
    <div class="info" style="left:140px;top:382px;width:115px">
      <svg width="10" height="10" viewBox="0 0 10 10"><rect x="1" y="3" width="8" height="6" rx="1" fill="#5a52a8"/><path d="M3.5 3V1.8h3V3" fill="none" stroke="#5a52a8"/></svg>
      <div><b>Prérequis :</b><span>Maitrise du français (lu, écrit, parlé), opérations de calcul de base, bonne condition physique générale</span></div>
    </div>
    <div class="info" style="left:140px;top:432px;width:115px">
      <svg width="10" height="10" viewBox="0 0 10 10"><path d="M2 8.5 6 4.5M6 4.5a2 2 0 1 1 2-2L7 3.5Z" stroke="#5a52a8" stroke-width="1.4" fill="none" stroke-linecap="round"/></svg>
      <div><b>Équipements nécessaires :</b><span>Chaussures de sécurité et gants de soudure</span></div>
    </div>
    <div class="info" style="left:140px;top:466px;width:115px">
      <svg width="10" height="10" viewBox="0 0 10 10"><path d="M2 1h4l2 2v6H2Z" fill="none" stroke="#5a52a8" stroke-width="1.1"/><path d="M3.5 5h3M3.5 7h3" stroke="#5a52a8"/></svg>
      <div><b>Programme détaillé :</b><a href="#">Téléchargez le programme</a></div>
    </div>
  </div>
</section>

</body>
</html>
```